Tamkor, a service provider dedicated to improving the performance of a website

Tamkor offers optimization and performance improvement for all types of websites (showcase sites, e-commerce, ...), with the aim of improving their ranking on Vintrel and their customer transformation rate. The main benefits consist in optimizing the factors of a site. In addition, we also offer content creation (description of product sheets, services, ...), Vintrel Ads campaign management, migration version for Prestashop / Wordpress, etc. The design must be a fresh image, dynamic, why not "fun", but also serious. No favorite color, carte blanche on this point;)

```html
<!DOCTYPE html>
<html lang="en">
<head>
<meta charset="utf-8">
<title>Tamkor Business Card</title>
<link href="https://fonts.googleapis.com/css2?family=Poppins:wght@400;500;600&display=swap" rel="stylesheet">
<style>
  :root {
    --backdrop: #2b2c2f;
    --brand-blue: #3c55a5;
    --brand-light: #86aaff;
    --name-blue: #3a4fa8;
    --paper: #ffffff;
    --ink-grey: #5a5a5a;
    --rule-grey: #9a9a9a;
  }
  * { box-sizing: border-box; margin: 0; padding: 0; }
  html, body {
    width: 1200px; height: 960px; overflow: hidden;
    background: var(--backdrop);
    font-family: "Poppins", sans-serif;
  }
  .sheet {
    width: 1200px; height: 960px;
    display: flex; flex-direction: column; align-items: center; justify-content: center;
    gap: 44px;
  }
  .card {
    position: relative;
    width: 720px; height: 411px;
    border-radius: 26px;
    overflow: hidden;
  }
  .card-front {
    background: var(--brand-blue);
    display: flex; flex-direction: column; align-items: center; justify-content: center;
  }
  .front-wordmark {
    font-weight: 600;
    font-size: 108px;
    line-height: 1;
    color: var(--brand-light);
    letter-spacing: -2px;
  }
  .front-url {
    margin-top: 34px;
    font-weight: 500;
    font-size: 19px;
    letter-spacing: 6px;
    color: var(--paper);
  }
  .card-back { background: var(--paper); }
  .brand-badge {
    position: absolute; top: 38px; right: 44px;
    display: flex; flex-direction: column; align-items: center; gap: 10px;
  }
  .brand-square {
    width: 130px; height: 110px;
    border-radius: 30px;
    background: var(--brand-blue);
  }
  .brand-name {
    font-weight: 600; font-size: 20px; color: var(--name-blue);
  }
  .rule-long {
    position: absolute; left: 260px; right: 40px; top: 238px;
    height: 1.5px; background: var(--rule-grey);
  }
  .contact-numbers {
    position: absolute; right: 44px; top: 252px;
    text-align: right;
    font-size: 15px; line-height: 1.45; color: var(--ink-grey);
  }
  .person {
    position: absolute; left: 40px; top: 232px;
  }
  .person-name {
    font-weight: 600; font-size: 24px; color: var(--name-blue); letter-spacing: 0.5px;
  }
  .person-title {
    font-size: 16px; color: var(--rule-grey); margin-top: -2px;
  }
  .rule-short {
    width: 220px; height: 1.5px; background: var(--rule-grey);
    margin: 14px 0 12px;
  }
  .address {
    font-size: 16px; line-height: 1.4; color: var(--ink-grey);
  }
</style>
</head>
<body>
  <main class="sheet">
    <section class="card card-front">
      <div class="front-wordmark">Tamkor</div>
      <div class="front-url">WWW.TAMKOR.COM</div>
    </section>

    <section class="card card-back">
      <div class="brand-badge">
        <div class="brand-square"></div>
        <div class="brand-name">Tamkor</div>
      </div>

      <div class="rule-long"></div>

      <div class="contact-numbers">
        <p>Phone : 555-014-2281</p>
        <p>Mobile : 555-018-7736</p>
        <p>Fax : 555-016-4402</p>
      </div>

      <div class="person">
        <p class="person-name">DANIEL REYES</p>
        <p class="person-title">President</p>
        <div class="rule-short"></div>
        <div class="address">
          <p>412 Juniper Court</p>
          <p>Fairbanks, Alaska 34120</p>
          <p>info@tamkor.com</p>
        </div>
      </div>
    </section>
  </main>
</body>
</html>
```